Personal Finance Author needs a postcard

Hi there,

I am a Canadian personal finance author and have published a new book called The Wealth Compass.

I teach Millennials how to create a 6-figure portfolio through investing (https://www.dariafelt.com/)

I'm speaking at some conferences so we were going to print some postcards to hand out to attendees with our info and calls-to-action on them.

I am looking for 4x6 (horizontal) postcard (no space needed for shipping label).

Logos, Headshots and Book Cover:
https://files.cloudvaultex.com/folders/8kQpZrT2mWvN4xLbJ7sHdYc3FgA9eUoRi?usp=sharing

Both sides will be full colour. I would like a clean and simple look. Our main sites are www.DariaFelt.com and www.TheWealthCompassBook.com if you want to get a sense of style and design.
I also uploaded a few marketing materials so you can see the existing designs.

Side 1:
Get Instant Access to your Free Resources - main headline

(small bullets underneath)
- The Wealth Compass Checklist
- Financial Worksheets
- Database of Investment Tools

DariaFelt.com/Resources

At the bottom, include "Don't forget to follow Daria Felt on social media:
Linkedin: @dariafelt7
Facebook: @thewealthcompassbook Instagram: @thewealthcompassbook Twitter: @WealthCompassBk"

Side 2:
Headline - Want to work directly with Daria and The Wealth Compass team to help you make your money grow and stay safe?

Work with us to (bullet point list)...
- Hire Daria as a Keynote Speaker
- Teach Financial Literacy Workshops
- Receive Financial Coaching

Want To Learn More About How We Can Help?
DariaFelt.com/Services

Include my contact info:
Daria Felt
Author | Speaker | Investor
daria@thewealthcompassbook.com
416-555-0187

Target Market(s)

Millennials who want to learn how to save and invest their money. I focus on stock market investing, real estate investing and entrepreneurship.

Industry/Entity Type

Financial Service

Font styles to use
Sans Serif

Colors

Designer to choose colors to be used in the design.

Requirements
Must have
• Photo of Daria Felt
• The Wealth Compass logo
• Green, Gold/Yellow to match existing colours
• modern business style postcard

```html
<!DOCTYPE html>
<html lang="en">
<head>
<meta charset="utf-8">
<title>The Wealth Compass – Postcard</title>
<link rel="stylesheet" href="https://fonts.googleapis.com/css2?family=Roboto+Condensed:wght@400;700&display=swap">
<style>
:root{
  --gold:#ebb526;
  --gold-deep:#e3a91c;
  --green:#0c5a2a;
  --green-text:#0e5e2b;
  --ink:#1e1e1e;
  --paper:#ececec;
  --stage:#636363;
  --white:#ffffff;
}
*{box-sizing:border-box;margin:0;padding:0}
html,body{width:947px;height:1200px;overflow:hidden}
body{background:var(--stage);font-family:"Roboto Condensed",Arial,sans-serif;position:relative}
.card{position:absolute;left:95px;width:758px;height:505px;overflow:hidden;box-shadow:0 4px 10px rgba(0,0,0,.35)}

/* Side 1 */
.side-resources{top:61px;background:linear-gradient(180deg,var(--gold) 0%,var(--gold-deep) 100%)}
.device{position:absolute;background:linear-gradient(160deg,#2a2a2a,#0d0d0d);border-radius:14px}
.device-tablet{left:100px;top:48px;width:241px;height:357px}
.device-phone{left:43px;top:179px;width:119px;height:245px;border-radius:16px}
.headline-band{position:absolute;left:341px;right:0;top:80px;height:170px;background:var(--green)}
.headline{position:absolute;left:377px;top:93px;color:var(--white);font-weight:700;font-size:44px;line-height:47px;text-transform:uppercase;letter-spacing:.5px;white-space:nowrap}
.resource-list{position:absolute;left:377px;top:264px;list-style:none}
.resource-list li{font-size:22px;line-height:30.5px;color:var(--ink);padding-left:14px;position:relative;white-space:nowrap}
.resource-list li::before{content:"";position:absolute;left:0;top:12px;width:6px;height:6px;border-radius:50%;background:var(--green)}
.resource-url{position:absolute;left:379px;top:377px;height:21px;padding:0 4px;border:1.5px solid var(--green);color:var(--green-text);font-weight:700;font-size:17px;line-height:18px;white-space:nowrap}
.follow-note{position:absolute;left:377px;top:424px;font-size:16px;color:var(--ink);white-space:nowrap}
.social-band{position:absolute;left:0;right:0;bottom:0;height:53px;background:var(--green);display:flex;align-items:center;justify-content:center;gap:12px}
.social{display:flex;align-items:center;gap:5px;color:var(--white);font-size:16px;white-space:nowrap}
.social-mark{width:13px;height:13px;background:var(--gold);border-radius:2px}

/* Side 2 */
.side-services{top:597px;background:linear-gradient(90deg,#eaeaea 0%,#efefef 60%,#e8e8e8 100%)}
.services-headline{position:absolute;left:38px;top:35px;color:var(--green-text);font-weight:700;font-size:25px;line-height:29.5px;text-transform:uppercase;white-space:nowrap}
.work-row{position:absolute;left:36px;top:142px;display:flex;gap:4px;height:30px}
.work-tag{height:30px;background:var(--gold);color:var(--green-text);font-weight:700;font-size:22px;line-height:30px;padding:0 5px;text-transform:uppercase;white-space:nowrap}
.work-tag-bar{width:4px;height:30px;background:var(--gold)}
.service-list{position:absolute;left:36px;top:189px;list-style:none}
.service-list li{font-size:22px;line-height:30.5px;color:var(--ink);padding-left:13px;position:relative;white-space:nowrap}
.service-list li::before{content:"";position:absolute;left:0;top:12px;width:6px;height:6px;border-radius:50%;background:var(--gold)}
.learn-more{position:absolute;left:40px;top:313px;font-size:16px;color:#333;white-space:nowrap}
.services-url{position:absolute;left:40px;top:335px;font-size:17px;font-weight:700;color:var(--green-text);white-space:nowrap}
.gold-rule{position:absolute;left:0;right:0;top:376px;height:8px;background:var(--gold)}
.contact-band{position:absolute;left:0;right:0;top:384px;bottom:0;background:var(--green)}
.contact{position:absolute;left:40px;top:394px;color:var(--white);white-space:nowrap}
.contact-name{font-weight:700;font-size:22px;line-height:25px}
.contact-role{font-size:18px;line-height:22px}
.contact-line{display:flex;align-items:center;gap:6px;font-size:18px;line-height:21px}
.contact-line svg{width:9px;height:9px;flex:none}
.book-cover{position:absolute;left:349px;top:279px;width:125px;height:205px;background:linear-gradient(160deg,#fafafa,#dcdcdc);box-shadow:2px 3px 8px rgba(0,0,0,.3)}
.author-photo{position:absolute;left:518px;top:35px;width:180px;height:455px;background:linear-gradient(180deg,#e4e4e4 0%,#2a2a2a 35%,#151515 100%);border-radius:40px 40px 4px 4px}
</style>
</head>
<body>

<section class="card side-resources">
  <div class="device device-tablet" role="img" aria-label="Tablet showing the Financial Goals worksheet"></div>
  <div class="device device-phone" role="img" aria-label="Phone showing the Monthly Budget worksheet"></div>

  <div class="headline-band"></div>
  <h1 class="headline">Get Instant<br>Access to Your<br>Free Resources</h1>

  <ul class="resource-list">
    <li>The Wealth Compass Checklist</li>
    <li>Financial Worksheets</li>
    <li>Database of Investment Tools</li>
  </ul>

  <div class="resource-url">DariaFelt.com/Resources</div>
  <p class="follow-note">Don't forget to follow Daria Felt on social media</p>

  <div class="social-band">
    <span class="social"><span class="social-mark"></span>@dariafelt7</span>
    <span class="social"><span class="social-mark"></span>@thewealthcompassbook</span>
    <span class="social"><span class="social-mark"></span>@thewealthcompassbook</span>
    <span class="social"><span class="social-mark"></span>@WealthCompassBk</span>
  </div>
</section>

<section class="card side-services">
  <h2 class="services-headline">Want to work directly with Daria and<br>The Wealth Compass team to help you<br>make your money grow and stay safe?</h2>

  <div class="work-row">
    <div class="work-tag">Work with us</div>
    <div class="work-tag-bar"></div>
  </div>

  <ul class="service-list">
    <li>Hire Daria as a Keynote Speaker</li>
    <li>Teach Financial Literacy Workshops</li>
    <li>Receive Financial Coaching</li>
  </ul>

  <p class="learn-more">Want To Learn More About How We Can Help?</p>
  <p class="services-url">DariaFelt.com/Services</p>

  <div class="gold-rule"></div>
  <div class="contact-band"></div>

  <div class="contact">
    <p class="contact-name">Daria Felt</p>
    <p class="contact-role">Author | Speaker | Investor</p>
    <p class="contact-line">
      <svg viewBox="0 0 10 10"><rect x="0.5" y="1.5" width="9" height="7" rx="1" fill="none" stroke="#ebb526" stroke-width="1.2"/><path d="M1 2.5 L5 5.5 L9 2.5" fill="none" stroke="#ebb526" stroke-width="1.2"/></svg>
      daria@thewealthcompassbook.com
    </p>
    <p class="contact-line">
      <svg viewBox="0 0 10 10"><rect width="10" height="10" rx="2" fill="#ebb526"/><path d="M3 2.2 C2.4 2.6 2.3 3.5 3 4.8 C3.8 6.3 5 7.5 6 7.8 C6.8 8 7.4 7.6 7.7 7.1 L6.6 6 L5.8 6.5 C5 6 4.3 5.2 3.9 4.3 L4.4 3.5 Z" fill="#0c5a2a"/></svg>
      416-555-0187
    </p>
  </div>

  <div class="book-cover" role="img" aria-label="Cover of the book The Wealth Compass by Daria Felt"></div>
  <div class="author-photo" role="img" aria-label="Photo of Daria Felt seated on a black chair in a dark suit"></div>
</section>

</body>
</html>
```